Fine Art Limited Edition Print Pop Up Shop

We do on day only pop up shops with the top master printmakers in South Africa. Its a fun day our for the whole family but with the focus on buying affordable limited edition lithographs from some of the country's most respected artists. There are food trucks and music and supervised art activities for the kids.
The Copperleaf Atelier Limited Edition Print Pop Up Shop offers Gauteng-based buyers the opportunity to purchase from the widest selection of prints on sale outside the studio’s White River, Mpumulanga premises. The Copperleaf Atelier is highly regarded for its work with both local and international artists who are invited to collaborate in the studio with Master Printer Peter Lindqvist.
With a particular focus on lithographs , monoprints and letterpress, the full range of The Copperleaf Atelier printmaking techniques will be on display at the Pop Up Shop through the work of more than 30 artists including Bruno Vellekoop, Marla Quint, Tiko Mabundabe, Gerrit Vanstaden , Henrik Ulsford, Pieter Rauch and Desmond Thokoane. There will also be brand new prints from from Marguerite Velthuisen, Lukas Fenwyck, Elsa Morbray, Helena Pryce and Liesel Crouwé. Prices range between R2 500 and R12 500
With plentiful parking, live music by The Velvet Lantern Choir and a small array of bespoke food trucks and beverages on site for the event, this short-term shop packed with long-term goods is not to be missed for both new buyers and those wanting to add to their collections.
Parents will be happy to know that once again there will be a supervised mono print activity for children of all ages on site. Under the guidance of printmakers from The Inkwell Forge Studio, children can try their hand at printmaking and take home what they make. The children’s printmaking at The Copperleaf Atelier Limited Edition Print Pop Up Shop is free.
Target Market(s)
fairly affluent people who have lovely homes and enough disposable income to afford to buy fine art
Industry/Entity Type
Shop
Requirements
Nice to have
- The poster should probably indicate that there is a wide range of artists and images available

```html
<!DOCTYPE html>
<html lang="en">
<head>
<meta charset="utf-8">
<title>The Copperleaf Atelier – Limited Edition Prints Pop Up Shop</title>
<link rel="stylesheet" href="https://fonts.googleapis.com/css2?family=Antonio:wght@200&family=Poppins:wght@300;600;700&display=swap">
<style>
  :root {
    --ink: #000000;
    --paper: #ffffff;
    --stone: #e9e6df;
  }
  html, body { margin: 0; padding: 0; width: 849px; height: 1200px; overflow: hidden; background: var(--paper); }
  .poster {
    position: relative; width: 1061px; height: 1500px;
    transform: scale(0.8); transform-origin: 0 0;
    background: var(--paper); overflow: hidden;
    font-family: "Poppins", sans-serif; color: var(--paper);
  }
  .block { position: absolute; }
  .black { background: var(--ink); }
  .artwork { position: absolute; }

  .brand-tile { display: flex; flex-direction: column; align-items: center; justify-content: center; gap: 8px; background: var(--paper); }
  .brand-tile .dot { width: 22px; height: 22px; border-radius: 50%; background: var(--ink); }
  .brand-tile .name { font-family: "Poppins", sans-serif; font-weight: 700; font-size: 19px; line-height: 1.15; color: var(--ink); text-align: center; letter-spacing: .02em; }

  .anniversary-badge { display: flex; align-items: center; justify-content: center; background: var(--paper); }

  .date { left: 177px; top: 219px; width: 353px; height: 94px; background: var(--ink); }
  .hours { left: 177px; top: 313px; width: 353px; height: 83px; background: var(--paper); }
  .date span, .hours span { position: absolute; left: 54px; font-weight: 700; font-size: 52px; letter-spacing: -.01em; line-height: 1; }
  .date span { top: 22px; color: var(--paper); }
  .hours span { top: 16px; color: var(--ink); }

  .info-panel { left: 177px; top: 396px; width: 707px; height: 529px; background: var(--ink); }
  .title {
    position: absolute; left: 56px; top: 58px; margin: 0; white-space: nowrap;
    font-family: "Antonio", sans-serif; font-weight: 200; font-size: 100px; line-height: 1;
    letter-spacing: .045em; text-transform: uppercase; transform: scaleX(.69); transform-origin: 0 0;
  }
  .dotted { position: absolute; border-left: 2px dotted #bdbdbd; }
  .subtitle { position: absolute; left: 111px; top: 198px; margin: 0; font-weight: 600; font-size: 29px; line-height: 38px; letter-spacing: .26em; text-transform: uppercase; }
  .lineup { position: absolute; left: 54px; top: 310px; margin: 0; font-weight: 300; font-size: 24px; line-height: 34px; letter-spacing: .045em; text-transform: uppercase; }
  .extras { position: absolute; left: 111px; top: 416px; margin: 0; font-weight: 600; font-size: 14px; line-height: 21px; letter-spacing: .16em; text-transform: uppercase; }

  .venue-panel { left: 530px; top: 1280px; width: 531px; height: 220px; background: var(--ink); }
  .venue-panel svg { position: absolute; left: 28px; top: 35px; }
  .venue-name { position: absolute; left: 56px; top: 30px; margin: 0; font-weight: 700; font-size: 25px; letter-spacing: .01em; }
  .venue-address { position: absolute; left: 56px; top: 67px; margin: 0; font-weight: 300; font-size: 23px; }
  .contact { position: absolute; left: 56px; top: 121px; margin: 0; font-weight: 700; font-size: 15px; line-height: 20px; letter-spacing: .09em; text-transform: uppercase; }
</style>
</head>
<body>
<main class="poster">

  <!-- Print grid -->
  <div class="block black" style="left:0;top:0;width:177px;height:42px"></div>
  <div class="block brand-tile" style="left:0;top:42px;width:177px;height:177px">
    <span class="dot"></span>
    <span class="name">The Copperleaf<br>Atelier</span>
  </div>

  <div class="artwork" role="img" aria-label="Print: seated ape with earring on red ground" style="left:177px;top:42px;width:177px;height:177px;background:linear-gradient(135deg,#8e1f22,#c9892d 60%,#e1b65a)"></div>
  <div class="artwork" role="img" aria-label="Print detail in amber brush strokes" style="left:354px;top:0;width:176px;height:42px;background:linear-gradient(90deg,#efe8d8,#6d4b2a,#efe8d8)"></div>
  <div class="artwork" role="img" aria-label="Print: dark sphere within a circular lace pattern" style="left:354px;top:42px;width:176px;height:177px;background:radial-gradient(circle,#333 0 28%,#9b9890 40%,#efece3 62%)"></div>
  <div class="artwork" role="img" aria-label="Print: figures on striped blue and pink ground" style="left:530px;top:42px;width:177px;height:177px;background:linear-gradient(160deg,#c9c2e6,#8a7fc7 45%,#cf6f7b 75%,#5a5faa)"></div>
  <div class="artwork" role="img" aria-label="Print: catalogue of insects on white" style="left:707px;top:0;width:177px;height:130px;background:linear-gradient(180deg,#f2f1ed,#bdbbb4)"></div>
  <div class="artwork" role="img" aria-label="Print: portrait drawn in red line" style="left:707px;top:130px;width:177px;height:176px;background:linear-gradient(135deg,#e2c9c6,#b8564f 55%,#7a2a27)"></div>
  <div class="artwork" role="img" aria-label="Print detail in orange and yellow" style="left:884px;top:0;width:177px;height:42px;background:linear-gradient(90deg,#e55a1d,#f1a21e)"></div>
  <div class="artwork" role="img" aria-label="Etching: windswept trees" style="left:884px;top:42px;width:177px;height:177px;background:linear-gradient(180deg,#f4f3ef,#b5b4ae 60%,#e9e8e4)"></div>

  <div class="artwork" role="img" aria-label="Etching: row of trees on a plain" style="left:0;top:219px;width:177px;height:177px;background:linear-gradient(180deg,#eeede8,#9d9c95 55%,#dedcd5)"></div>
  <div class="artwork" role="img" aria-label="Print: animal in bow tie on cobalt ground" style="left:530px;top:219px;width:177px;height:177px;background:linear-gradient(135deg,#1f2fa5,#2a44c8 45%,#9d9a82 70%,#e3c33c)"></div>
  <div class="block black" style="left:707px;top:306px;width:177px;height:90px"></div>

  <div class="block anniversary-badge" style="left:884px;top:306px;width:177px;height:179px">
    <svg width="150" height="150" viewBox="0 0 150 150" aria-hidden="true">
      <circle cx="75" cy="75" r="71" fill="none" stroke="#000" stroke-width="5"/>
      <circle cx="75" cy="75" r="46" fill="none" stroke="#000" stroke-width="3"/>
    </svg>
  </div>

  <div class="artwork" role="img" aria-label="Print: horned skull above a burning pyre" style="left:0;top:485px;width:177px;height:175px;background:linear-gradient(180deg,#e9a48e,#e48069 45%,#6e3a2b 75%,#d85a35)"></div>
  <div class="artwork" role="img" aria-label="Print: interior with painting and blue sofa" style="left:0;top:660px;width:177px;height:178px;background:linear-gradient(180deg,#efeeeb,#e6e4df 35%,#caa43f 45%,#efeeeb 60%,#2c47a8 85%,#efeeeb)"></div>
  <div class="artwork" role="img" aria-label="Print: flowering aloe" style="left:0;top:838px;width:177px;height:177px;background:linear-gradient(180deg,#f5f4f0,#e2d7b7 50%,#5f8a3f 95%)"></div>
  <div class="block black" style="left:0;top:1015px;width:177px;height:87px"></div>
  <div class="artwork" role="img" aria-label="Print: skull within a circular dotted pattern" style="left:0;top:1102px;width:177px;height:178px;background:radial-gradient(circle,#2c2c2c 0 30%,#8f8d88 45%,#f1efe9 66%)"></div>
  <div class="artwork" role="img" aria-label="Print: seated ape in grey and ochre" style="left:0;top:1280px;width:177px;height:177px;background:linear-gradient(135deg,#c8b49a,#8f7a66 50%,#2a3256)"></div>
  <div class="block black" style="left:0;top:1457px;width:177px;height:43px"></div>

  <div class="artwork" role="img" aria-label="Print: three figures on green patterned ground" style="left:884px;top:485px;width:177px;height:175px;background:linear-gradient(135deg,#9ec27c,#c56048 45%,#b8d08d 70%,#5b7ca0)"></div>
  <div class="block black" style="left:884px;top:660px;width:177px;height:88px"></div>
  <div class="artwork" role="img" aria-label="Drawing: tumbling figures and animals in graphite" style="left:884px;top:748px;width:177px;height:177px;background:linear-gradient(135deg,#f0efec,#8c8a85 50%,#ececea)"></div>

  <div class="artwork" role="img" aria-label="Print: white line form on dark ground" style="left:177px;top:925px;width:177px;height:177px;background:radial-gradient(circle,#5b5a63,#232228 70%)"></div>
  <div class="artwork" role="img" aria-label="Print: mother holding two babies" style="left:354px;top:1010px;width:176px;height:177px;background:linear-gradient(180deg,#e9e6e2,#b98a6a 45%,#b24a43 75%,#d7d3cf)"></div>
  <div class="artwork" role="img" aria-label="Print: ape wearing a cross pendant" style="left:530px;top:925px;width:177px;height:177px;background:linear-gradient(135deg,#dedbd4,#6d665e 50%,#a19789)"></div>
  <div class="artwork" role="img" aria-label="Print: pink figure with bird on orange ground" style="left:707px;top:925px;width:177px;height:177px;background:linear-gradient(135deg,#e0602e,#e99378 45%,#a9512f 70%,#d2b43d)"></div>
  <div class="artwork" role="img" aria-label="Print: pale ape on black ground" style="left:884px;top:925px;width:177px;height:177px;background:radial-gradient(circle,#bdb5a3 0 35%,#3a3a3c 60%,#111 90%)"></div>

  <div class="artwork" role="img" aria-label="Etching: tall cactus" style="left:177px;top:1102px;width:177px;height:178px;background:linear-gradient(180deg,#f6f5f2,#a9a7a0 55%,#f1f0ec)"></div>
  <div class="artwork" role="img" aria-label="Print: interior with pink wall and red chair" style="left:354px;top:1187px;width:176px;height:175px;background:linear-gradient(180deg,#e7c9d4,#d77b9a 40%,#c8232a 70%,#a2202a)"></div>
  <div class="artwork" role="img" aria-label="Print: flowering desert rose plant" style="left:530px;top:1102px;width:177px;height:178px;background:linear-gradient(180deg,#f5f4ef,#7e9a5c 55%,#c9b9a5)"></div>
  <div class="artwork" role="img" aria-label="Print: reclining figure in red line" style="left:707px;top:1102px;width:177px;height:178px;background:linear-gradient(135deg,#8d3b3b,#b4868a 50%,#5b3e4e)"></div>
  <div class="artwork" role="img" aria-label="Print: profile head in dark strokes" style="left:884px;top:1102px;width:177px;height:178px;background:linear-gradient(90deg,#c9c4b8,#3a2a1e 45%,#7a5c3c)"></div>
  <div class="artwork" role="img" aria-label="Print: seated figure on green patterned ground" style="left:177px;top:1280px;width:177px;height:177px;background:linear-gradient(135deg,#6fa0a3,#b9c7c0 50%,#7e8c99)"></div>
  <div class="artwork" role="img" aria-label="Print: burst of coloured lines" style="left:354px;top:1362px;width:176px;height:138px;background:linear-gradient(135deg,#8ac7b5,#f2c73c 50%,#e3573a 80%)"></div>

  <!-- Date and hours -->
  <div class="block date"><span>03.10.16</span></div>
  <div class="block hours"><span>9h &gt; 16h</span></div>

  <!-- Main information -->
  <section class="block info-panel">
    <h1 class="title">The Copperleaf Atelier</h1>
    <span class="dotted" style="left:82px;top:203px;height:68px"></span>
    <p class="subtitle">Limited Edition<br>Prints Pop Up Shop</p>
    <p class="lineup">Artists and master print makers<br>with live music by The Velvet Lantern Choir</p>
    <span class="dotted" style="left:82px;top:421px;height:36px"></span>
    <p class="extras">Besboke food trucks and beverages on site<br>Free supervised printmaking workshop for kids</p>
  </section>

  <!-- Venue -->
  <section class="block venue-panel">
    <svg width="16" height="22" viewBox="0 0 16 22" aria-hidden="true">
      <path d="M2 1h12v2h-2v7l3 3v2H9v7H7v-7H1v-2l3-3V3H2z" fill="#fff"/>
    </svg>
    <p class="venue-name">Westcliff Ridge School for Girls</p>
    <p class="venue-address">18 Marlow Avenue, Greenhill</p>
    <p class="contact">Contact : info@copperleafatelier.co.za<br>011 555 0192</p>
  </section>

</main>
</body>
</html>
```